SINGLE PAGE WEBSITE needed for Haunted-House Style Horror Event!

PROJECT:
Single page website to advertise "Bolting Shadows"

ABOUT BOLTING SHADOWS:
Bolting Shadows is a Horror Experience event, that will be held on June 1st 2019 at The Ember Playhouse in Sydney.

At the event, patrons will enter 6 different rooms and have a horror experience in each one.

There's a bar on-site for them to drink as well.

NEEDS FOR THE WEBSITE:
1. Video banner at top, and scrolling photos after video finishes, and text over the top of the video with the name and date of the event
eg.
"A Night of Immersive Horror Experiences"
"The Ember Playhouse | June 1st, 2019"

2. Multiple Book Now buttons on the page, which will link to an external booking platform

3. It should say somewhere "Produced by [MARBLE LANTERN PRODUCTIONS LOGO]"

4. A "Next Steps" section that has the steps for them to complete, such as
- Purchase your ticket HERE for one of our waves
- Rock up at the Ember Playhouse on June 1st at your wave time
- Experience each of our 6 Interactive Horror Rooms
- Grab some drinks at the bar, a bite to eat, and enjoy a fantastic night out!

Other things that should be included somewhere:
- Testimonials
- FAQs (maybe as a dropdown, so it doesn't take up much space?)
- Contact Form on Footer

- - - -

Images, logos, and more attached!

Industry/Entity Type

Events

Coding

Coded - Design and coding required

Number of Pages Required

1 page

Requirements
Nice to have
• 1. Video banner at top, and scrolling photos after video finishes, and text over the top of the video with the name and date of the event
• eg.
• "A Night of Immersive Horror Experiences"
• "The Ember Playhouse | June 1st, 2019"
• 2. multiple Book Now buttons on the page, which will link to an external booking platform
• 3. It should say somewhere "Produced by [Marble Lantern Productions LOGO]" with the Marble Lantern logo
• 4. A "Next Steps" section that has the steps for them to complete, such as
• - Purchase your ticket HERE for one of our waves
• - Rock up at the Ember Playhouse on June 1st at your wave time
• - Experience each of our 6 Interactive Horror Rooms
• - Grab some drinks at the bar, a bite to eat, and enjoy a fantastic night out!
• Other things that should be included somewhere:
• - Testimonials
• - FAQs (maybe as a dropdown, so it doesn't take up much space?)
• - Contact Form on Footer

```html
<!DOCTYPE html>
<html lang="en">
<head>
<meta charset="utf-8">
<title>Bolting Shadows — A Night of Immersive Horror Experiences</title>
<link rel="stylesheet" href="https://fonts.googleapis.com/css2?family=Coustard:wght@400;900&family=Roboto:wght@400;500;700;900&display=swap">
<style>
  :root{
    --lime:#a2c523;
    --lime-deep:#8fb115;
    --ink:#0c0b0d;
    --night:#121113;
    --panel:#1e1c1f;
    --panel-open:#141315;
    --field:#060606;
    --text:#f2f2f2;
    --muted:#b9b9b9;
    --heading:"Coustard", Georgia, serif;
    --body:"Roboto", Arial, sans-serif;
  }
  *{box-sizing:border-box;margin:0;padding:0}
  html,body{width:1200px;height:3152px;overflow:hidden}
  body{background:var(--ink);color:var(--text);font-family:var(--body);position:relative}
  section,header,footer{position:absolute;left:0;width:1200px}
  .abs{position:absolute}
  .section-title{font-family:var(--heading);font-weight:900;color:#fff8e6;font-size:40px;text-align:center;width:100%;position:absolute;left:0;letter-spacing:.5px}
  .btn{position:absolute;background:var(--lime);color:#111;font:700 12px/1 var(--body);letter-spacing:.5px;text-transform:uppercase;display:flex;align-items:center;justify-content:center;text-decoration:none}

  /* Hero */
  .hero{top:0;height:578px;overflow:hidden}
  .hero-media{position:absolute;inset:0;background:
    radial-gradient(ellipse 260px 320px at 340px 300px,#5a3b33 0%,#2a1c1a 55%,transparent 80%),
    radial-gradient(ellipse 300px 340px at 860px 300px,#7a5a3c 0%,#3a2a1e 50%,transparent 80%),
    linear-gradient(#0b0a0b,#1a1414 50%,#0d0b0b)}
  .hero-shade{position:absolute;inset:0;background:linear-gradient(rgba(0,0,0,.55),rgba(0,0,0,.25) 40%,rgba(0,0,0,.6))}
  .brand{left:252px;top:17px;width:194px;height:59px;display:flex;align-items:center;gap:10px;font:900 20px/1 var(--body);color:var(--lime);text-transform:uppercase;letter-spacing:.5px}
  .brand-mark{width:16px;height:16px;background:var(--lime)}
  .nav{left:557px;top:29px;height:34px;display:flex;align-items:center;gap:0;font:700 11px/1 var(--body);color:#fff;text-transform:uppercase}
  .nav a{color:#fff;text-decoration:none;position:absolute;white-space:nowrap}
  .hero-title{top:232px;width:100%;text-align:center;font-family:var(--heading);font-weight:900;font-size:46px;line-height:48px;color:#fff8e6}
  .hero-date{left:450px;top:347px;width:300px;height:35px;background:var(--lime);color:#111;font:700 17px/35px var(--body);text-align:center}
  .slider-dots{left:567px;top:549px;display:flex;gap:5px}
  .slider-dots span{width:11px;height:11px;border-radius:50%;background:var(--lime)}
  .slider-dots .active{background:transparent;border:2px solid var(--lime)}

  /* Steps */
  .steps{top:578px;height:862px;background:var(--night)}
  .step{position:absolute;display:flex;align-items:center;gap:26px}
  .step-icon{width:92px;height:92px;flex:none}
  .step-text{font:700 17px/23px var(--body);color:#fff;width:290px}
  .step-text mark{background:var(--lime);color:#111;padding:0 2px}

  /* Testimonials */
  .testimonials{top:1440px;height:430px;overflow:hidden}
  .testimonials-media{position:absolute;inset:0;background:
    radial-gradient(ellipse 380px 200px at 600px 260px,#4a3b34,transparent 75%),
    radial-gradient(ellipse 200px 200px at 180px 120px,#3b2326,transparent 75%),
    linear-gradient(90deg,#1c1719,#2a2224 50%,#1a1618)}
  .testimonials-shade{position:absolute;inset:0;background:rgba(0,0,0,.45)}
  .quote-mark{left:0;width:100%;top:1598px}
  .quote{left:311px;top:1657px;width:580px;text-align:center;font:700 13px/23px var(--body);color:#fff}
  .author{left:540px;top:1751px;display:flex;align-items:center;gap:10px;font:700 13px/1 var(--body)}
  .avatar{width:36px;height:36px;border-radius:50%;background:linear-gradient(#c9b7a8,#8c7668);border:2px solid #fff}

  /* FAQ */
  .faq{top:1870px;height:641px;background:var(--night)}
  .faq-item{position:absolute;left:250px;width:700px;background:var(--panel);border:1px solid #2c2a2d}
  .faq-q{height:38px;display:flex;align-items:center;justify-content:space-between;padding:0 12px;font:700 12px/1 var(--body);color:#d6d6d6}
  .faq-item.open .faq-q{color:#fff;border-bottom:1px solid #333}
  .faq-toggle{color:var(--lime);font:700 16px/1 var(--body)}
  .faq-a{background:var(--panel-open);padding:10px 12px 12px;font:400 11px/16px var(--body);color:#cfcfcf;height:79px}

  /* Contact */
  .contact{top:2511px;height:463px;overflow:hidden}
  .contact-media{position:absolute;inset:0;background:
    radial-gradient(ellipse 260px 300px at 570px 230px,#3a322c,transparent 75%),
    radial-gradient(ellipse 260px 280px at 1020px 300px,#5a2a24,transparent 75%),
    radial-gradient(ellipse 220px 260px at 120px 200px,#352526,transparent 75%),
    linear-gradient(#1a1718,#100e0f)}
  .contact-shade{position:absolute;inset:0;background:rgba(0,0,0,.45)}
  .field{position:absolute;background:var(--field);font:700 11px/1 var(--body);color:#fff;padding:10px 8px}

  /* Footer */
  .site-footer{top:2974px;height:178px;background:#000;text-align:center}
  .produced{top:35px;width:100%;font:700 19px/1 var(--body);color:#fff}
  .producer{top:66px;width:100%;display:flex;justify-content:center;align-items:center;gap:10px;font:900 16px/1 var(--body);color:#d9d9d9;letter-spacing:1px}
  .producer-mark{width:14px;height:14px;background:#d9d9d9}
  .copyright{top:151px;width:100%;font:400 10px/1 var(--body);color:#ddd}
  .copyright span{color:var(--lime)}
</style>
</head>
<body>

<header class="hero">
  <div class="hero-media" role="img" aria-label="Banner video of two made-up horror performers in a dark theatre"></div>
  <div class="hero-shade"></div>
  <a class="brand abs" href="#"><span class="brand-mark"></span>Bolting Shadows</a>
  <nav class="nav abs" style="width:400px">
    <a href="#what-to-do" style="left:0;top:11px">What To Do</a>
    <a href="#testimonials" style="left:82px;top:11px">Testimonials</a>
    <a href="#faq" style="left:176px;top:11px">FAQ</a>
    <a href="#contact" style="left:216px;top:11px">Contact Us</a>
  </nav>
  <a class="btn" href="#" style="left:860px;top:29px;width:90px;height:34px">Get Tickets</a>
  <h1 class="hero-title abs">A Night of Immersive<br>Horror Experiences</h1>
  <div class="hero-date abs">The Ember Playhouse | June 1st, 2019</div>
  <div class="slider-dots abs"><span></span><span></span><span class="active"></span><span></span><span></span></div>
</header>

<section class="steps" id="what-to-do">
  <h2 class="section-title" style="top:60px">What To Do</h2>

  <div class="step" style="left:311px;top:147px">
    <svg class="step-icon" viewBox="0 0 92 92"><circle cx="46" cy="46" r="44" fill="var(--lime)"/>
      <g transform="rotate(-25 46 46)"><rect x="30" y="26" width="32" height="42" rx="3" fill="#111"/><line x1="34" y1="40" x2="58" y2="40" stroke="var(--lime)" stroke-width="2" stroke-dasharray="3 3"/><rect x="37" y="47" width="18" height="3" fill="var(--lime)"/><rect x="37" y="54" width="18" height="3" fill="var(--lime)"/></g></svg>
    <p class="step-text">Purchase your ticket <mark>here</mark> for one of our waves</p>
  </div>

  <div class="step" style="left:490px;top:294px">
    <svg class="step-icon" viewBox="0 0 92 92"><circle cx="46" cy="46" r="44" fill="var(--lime)"/>
      <rect x="26" y="28" width="40" height="38" rx="3" fill="#111"/><rect x="30" y="38" width="32" height="24" fill="var(--lime)"/><rect x="33" y="23" width="4" height="10" fill="#111"/><rect x="55" y="23" width="4" height="10" fill="#111"/>
      <text x="46" y="58" text-anchor="middle" font-family="Roboto, Arial, sans-serif" font-weight="900" font-size="18" fill="#111">1</text></svg>
    <p class="step-text">Rock up at the <mark>Ember Playhouse</mark> on June 1st at your wave time</p>
  </div>

  <div class="step" style="left:311px;top:437px">
    <svg class="step-icon" viewBox="0 0 92 92"><circle cx="46" cy="46" r="44" fill="var(--lime)"/>
      <path d="M30 66 V44 a16 16 0 0 1 32 0 V66 l-5 -5 -5 5 -6 -5 -6 5 -5 -5 z" fill="#111"/></svg>
    <p class="step-text">Experience each of our 6 Interactive Horror Rooms</p>
  </div>

  <div class="step" style="left:490px;top:574px">
    <svg class="step-icon" viewBox="0 0 92 92"><circle cx="46" cy="46" r="44" fill="var(--lime)"/>
      <rect x="30" y="30" width="26" height="36" rx="3" fill="#111"/><path d="M56 38 h6 a5 5 0 0 1 5 5 v10 a5 5 0 0 1 -5 5 h-6" fill="none" stroke="#111" stroke-width="4"/><rect x="35" y="38" width="3" height="22" fill="var(--lime)"/><rect x="42" y="38" width="3" height="22" fill="var(--lime)"/><rect x="49" y="38" width="3" height="22" fill="var(--lime)"/></svg>
    <p class="step-text">Grab some drinks at the bar, a bite to eat, and enjoy a fantastic night out!</p>
  </div>

  <a class="btn" href="#" style="left:542px;top:748px;width:118px;height:40px">Get Tickets</a>
</section>

<section class="testimonials" id="testimonials">
  <div class="testimonials-media" role="img" aria-label="Photo of a group of event guests posing with performers in front of a painted horror mural"></div>
  <div class="testimonials-shade"></div>
  <h2 class="section-title" style="top:48px">Testimonials</h2>
</section>
<svg class="abs quote-mark" height="40" viewBox="0 0 1200 40"><g fill="var(--lime)"><path d="M582 4 h14 l-6 16 h6 v18 h-18 v-16 z"/><path d="M604 4 h14 l-6 16 h6 v18 h-18 v-16 z"/></g></svg>
<p class="quote abs">Saepe verterem te quo. Ea fugit platonem expetenda mel. Latine vocibus persecuti ne quo, ad qui libris eripuit omittantur. Illud tamquam evertitur eos ea. Usu pericula disputando no, appetere iracundia pri ut. Mutat labore accommodare et vim, docendi qualisque inciderint duo no.</p>
<div class="author abs"><span class="avatar"></span>Mara Quill</div>
<svg class="abs" style="left:256px;top:1683px" width="14" height="18" viewBox="0 0 14 18"><path d="M11 2 L4 9 L11 16" fill="none" stroke="var(--lime)" stroke-width="3"/></svg>
<svg class="abs" style="left:928px;top:1683px" width="14" height="18" viewBox="0 0 14 18"><path d="M3 2 L10 9 L3 16" fill="none" stroke="var(--lime)" stroke-width="3"/></svg>

<section class="faq" id="faq">
  <h2 class="section-title" style="top:78px">FAQ</h2>
  <div class="faq-item open" style="top:156px">
    <div class="faq-q">Vix id munere neglegentur, eu duo justo assum everti, duo no probo voluptatum?<span class="faq-toggle">–</span></div>
    <div class="faq-a">Lorem ipsum dolor sit amet, his ex amet erat consulatu. Vix id munere neglegentur, eu duo justo assum everti, duo no probo voluptatum. Munere dolorum eleifend nec ei, rebum exerci ubique nec no, usu ea sale quas bonorum. Vim id liber dolorem repudiare. Te modus mnesarchum interesset mel, vix ea altera repudiandae. Vim illum antiopam an.</div>
  </div>
  <div class="faq-item" style="top:280px"><div class="faq-q">Et voluptua explicari disputationi eum ex elitr insolens postulant, eos bonorum facilis at?<span class="faq-toggle">+</span></div></div>
  <div class="faq-item" style="top:324px"><div class="faq-q">Minimum electram ex ius, usu et iisque legimus tota consectetuer ut per appetere?<span class="faq-toggle">+</span></div></div>
  <div class="faq-item" style="top:368px"><div class="faq-q">Est et meis expetendis, vis no odio graeci delicata duo minimum sensibus pericula cu?<span class="faq-toggle">+</span></div></div>
  <div class="faq-item" style="top:412px"><div class="faq-q">Ei virtute debitis per ceteros abhorreant argumentum vel in?<span class="faq-toggle">+</span></div></div>
  <a class="btn" href="#" style="left:542px;top:502px;width:118px;height:38px">Get Tickets</a>
</section>

<section class="contact" id="contact">
  <div class="contact-media" role="img" aria-label="Dim photo of costumed horror performers in a dark room"></div>
  <div class="contact-shade"></div>
  <h2 class="section-title" style="top:70px">Contact Us</h2>
  <div class="field" style="left:250px;top:149px;width:219px;height:37px">Name*</div>
  <div class="field" style="left:490px;top:149px;width:220px;height:37px">Email*</div>
  <div class="field" style="left:731px;top:149px;width:219px;height:37px">Subject</div>
  <div class="field" style="left:250px;top:200px;width:700px;height:116px">Message</div>
  <a class="btn" href="#" style="left:847px;top:334px;width:103px;height:36px">Submit</a>
</section>

<footer class="site-footer">
  <p class="produced abs">Produced by</p>
  <div class="producer abs"><span class="producer-mark"></span>MARBLE LANTERN PRODUCTIONS</div>
  <p class="copyright abs">Copyright © 2019 <span>Marble Lantern Productions</span></p>
</footer>

</body>
</html>
```